International Health Supplement Company Needs Packaging and Label Redesign

Copperfield Vitals LLC requires a redesign for 1 internationally sold product and accompanying designs for 5 additional products. The additional products are currently sold locally and yet to be released internationally.

Our company is honest, premium, and passionate about supplements. We adopt a 'no BS' stance and as such source only the finest ingredients and deliver high-quality liquid health supplements to customers globally. We do not compromise on quality and do not apologise for price.

We want a clean, crisp design that conveys ‘premium, cutting-edge, boutique’ at a glance. We feel our current design appeals more to the 'chest beaters' rather than the 'chess players' that our research has indicated are our customers.

We have SIX PRODUCTS TOTAL in our range and feel individual color cues to distinguish the different products would greatly assist customer navigation i.e. Customers will identify ‘red’ means ‘product X’ without reading the label. (Examples attached and below we believe do this well).

Current 30ml bottle, cap, and dropper are in black and will remain so. Current label is black, however, we have a white label on our local product (example attached) and prefer the look of it.

Packaging is currently black and could remain so however most products that appeal to our target market are in white with color accents.

One consideration we have is that the product up until now has been selling exceptionally well so we need to retain some kind of familiarity with the existing branding. Perhaps that’s just the logo.

Logo can be revised i.e. add company name and/or company slogan.

Products are: (Function - Name)

Testosterone Support - Tongkat Ali (current)
Hormone Support - Jiaogulan
Energy Support - Ashwaghanda
Libido Support - Krachai Dam (for men)
Libido Support - Kacip Fatimah (for women)
Sleep Support - Wild Chamomile

Packaging: 4.6cm (L) x 8.0cm (W) x 11.2cm (H)
Label: 30 mL bottle

https://www.portfolioshelf.example/gallery/TONIC-BOX-STUDY-2012/8824160
http://www.pelrostudio.example/projects/#/harbor-tea/
https://www.portfolioshelf.example/gallery/57730482/Velmora-Skin
https://au.pinboardly.example/pin/913402775610238841/
https://au.pinboardly.example/pin/61470329814550298/
http://kelvo.studio.example/en/portfolio/logo-redesign/

Target Market(s)

Generation X Men (and their partners), 36-55, upper middle class, who appreciate quality products.

Industry/Entity Type

Health Product

Font styles to use
Serif
Sans Serif

Requirements
Must have
• Packaging - Principal Display Panel (Front):
• 1. Function & Name of each product i.e 'Testosterone Support' & 'Tongkat Ali'
• 2. '30ml' AND '1 fl oz' (text size 1.8in / 3.2mm / 9 point min.)
• 3. 'Dietary Supplement'
• Packaging - Information Panel (Right):
• 1. Supplement Facts Panel (template accepted for drafts)
• 2. Directions: (lorum ipsum accepted for drafts)
• 3. Safety Warning: (lorum ipsum accepted for drafts)
• 4. 'Manufactured for: Copperfield Vitals LLC'
• 5. 'Sheridan, Wyoming'
• 6. '(307) 641 3528'
• 7. 'Product of Thailand'
• Bottle Label:
• 3. 'Dietary Supplement'
• 4. Supplement Facts Panel (template accepted for drafts)
• 5. Directions: (lorum ipsum accepted for drafts)
• 6. Safety Warning: (forum ipsum accepted for drafts)
• 7. 'Manufactured for: Copperfield Vitals LLC'
• 8. 'Sheridan, Wyoming'
• 9. '(307) 641 3528'
• 10. 'Product of Thailand'
Nice to have
• Updated logo with company name 'Copperfield Vitals' and/or company slogan 'Crafted With Quiet Care' added.
Should not have
• No photos or stock images.
• No elements of the current design (excluding logo) to remain i.e. 'Otter Finn', 'Testosterone Booster', 'Increase Lean Muscle', 'Stabilise Hormones', 'Boost Endurance', 'Improve Muscle Naturally', are all to be omitted.

```html
<!DOCTYPE html>
<html lang="en">
<head>
<meta charset="utf-8">
<title>Copperfield Vitals – Testosterone Support packaging</title>
<link rel="stylesheet" href="https://fonts.googleapis.com/css2?family=Archivo+Black&family=Open+Sans:ital,wght@0,400;0,600;1,300&family=Raleway:wght@400;500&family=Roboto+Condensed:wght@400;700&display=swap">
<style>
  :root {
    --red: #e41e26;
    --ink: #2b2b2b;
    --grey: #6d6d6d;
    --paper: #ffffff;
    --canvas: #f1f1f1;
    --faint: #e6e6e6;
  }
  * { box-sizing: border-box; margin: 0; padding: 0; }
  html, body { width: 762px; height: 1200px; overflow: hidden; }
  body { background: var(--canvas); position: relative; font-family: "Open Sans", sans-serif; color: var(--ink); }

  /* shared brand wordmark */
  .brand-name { font-family: "Raleway", sans-serif; font-weight: 500; color: var(--ink); letter-spacing: .02em; text-transform: uppercase; white-space: nowrap; }
  .tagline { font-family: "Raleway", sans-serif; color: var(--grey); letter-spacing: .03em; white-space: nowrap; }
  .function { font-family: "Open Sans", sans-serif; font-weight: 600; text-transform: uppercase; line-height: 1.12; color: var(--ink); }
  .rule { height: 2px; background: var(--red); }
  .herb { font-family: "Open Sans", sans-serif; font-style: italic; font-weight: 300; color: var(--grey); letter-spacing: .06em; }
  .category { font-family: "Open Sans", sans-serif; color: var(--grey); }
  .volume { font-family: "Open Sans", sans-serif; color: var(--red); }
  .molecule-art { position: absolute; background: radial-gradient(ellipse at 40% 45%, rgba(150,150,150,.28), rgba(200,200,200,.08) 65%, transparent 80%); }

  /* bottle label, flat */
  .bottle-label { position: absolute; left: 201px; top: 113px; width: 360px; height: 500px; background: var(--paper); border-left: 6px solid var(--red); box-shadow: 0 1px 4px rgba(0,0,0,.12); }
  .bottle-label .brand-name { position: absolute; left: 30px; top: 60px; font-size: 22px; }
  .bottle-label .function { position: absolute; left: 30px; top: 228px; font-size: 28px; }
  .bottle-label .rule { position: absolute; left: 30px; top: 308px; width: 290px; }
  .bottle-label .herb { position: absolute; left: 30px; top: 320px; font-size: 24px; }
  .bottle-label .category { position: absolute; left: 30px; top: 410px; font-size: 19px; }
  .bottle-label .volume { position: absolute; left: 30px; top: 438px; font-size: 22px; }

  /* box dieline, flat */
  .dieline { position: absolute; left: 11px; top: 683px; width: 740px; height: 404px; }
  .panel { position: absolute; overflow: hidden; }
  .flap-top { left: 132px; top: 0; width: 230px; height: 52px; background: var(--red); }
  .flap-bottom { left: 132px; top: 374px; width: 230px; height: 30px; background: var(--red); }
  .side-left { left: 0; top: 52px; width: 132px; height: 322px; background: var(--red); }
  .front { left: 132px; top: 52px; width: 230px; height: 322px; background: var(--paper); }
  .info { left: 362px; top: 52px; width: 135px; height: 322px; background: var(--paper); border-left: 1px solid var(--faint); }
  .facts-panel { left: 497px; top: 52px; width: 243px; height: 322px; background: var(--paper); border-left: 1px solid var(--faint); }

  .front .brand-name { position: absolute; left: 22px; top: 32px; font-size: 13.5px; }
  .front .brand-rule { position: absolute; left: 22px; top: 52px; width: 180px; height: 1px; background: var(--red); }
  .front .tagline { position: absolute; left: 22px; top: 56px; font-size: 9px; }
  .front .function { position: absolute; left: 22px; top: 176px; font-size: 14px; }
  .front .rule { position: absolute; left: 22px; top: 215px; width: 180px; }
  .front .herb { position: absolute; left: 22px; top: 222px; font-size: 13.5px; }
  .front .category { position: absolute; left: 22px; top: 280px; font-size: 11px; }
  .front .volume { position: absolute; left: 22px; top: 298px; font-size: 13px; }

  .info-copy { padding: 20px 8px 0 10px; font-family: "Roboto Condensed", sans-serif; font-size: 7.6px; line-height: 1.32; color: var(--ink); text-align: justify; }
  .info-copy p + p { margin-top: 6px; }
  .info-copy strong { color: var(--red); font-weight: 700; }

  .facts { margin: 12px 10px 0; border: 1.5px solid var(--ink); padding: 3px 5px 4px; font-family: "Roboto Condensed", sans-serif; font-size: 6.4px; }
  .facts-title { font-family: "Archivo Black", sans-serif; font-size: 17px; line-height: 1.05; letter-spacing: -.01em; }
  .facts-serving { border-bottom: 4px solid var(--ink); padding-bottom: 2px; line-height: 1.4; }
  .facts table { width: 100%; border-collapse: collapse; }
  .facts th, .facts td { text-align: left; padding: 1px 0; border-bottom: .5px solid #999; font-weight: 400; }
  .facts th { font-weight: 700; border-bottom: 1.5px solid var(--ink); }
  .facts .dv { text-align: right; }
  .facts .indent { padding-left: 8px; }
  .facts-note { margin-top: 2px; font-size: 5.4px; }
  .panel-notes { margin: 6px 10px 0; font-family: "Roboto Condensed", sans-serif; font-size: 6.8px; line-height: 1.35; color: var(--grey); }
  .panel-notes p + p { margin-top: 5px; }
  .storage { text-transform: uppercase; }
  .maker { position: absolute; left: 10px; top: 250px; font-family: "Roboto Condensed", sans-serif; font-size: 6.8px; line-height: 1.35; color: var(--grey); }
  .origin { position: absolute; left: 10px; bottom: 12px; font-family: "Roboto Condensed", sans-serif; font-size: 6.8px; color: var(--grey); }
</style>
</head>
<body>

  <section class="bottle-label" aria-label="Bottle label">
    <div class="molecule-art" style="left:150px;top:120px;width:200px;height:170px" role="img" aria-label="Faint grey molecular structure backdrop"></div>
    <p class="brand-name">Copperfield Vitals</p>
    <h1 class="function">Testosterone<br>Support</h1>
    <div class="rule"></div>
    <p class="herb">Tongkat Ali</p>
    <p class="category">Dietary Supplement</p>
    <p class="volume">30ml / 1 fl oz</p>
  </section>

  <section class="dieline" aria-label="Box dieline">
    <div class="panel flap-top"></div>
    <div class="panel side-left">
      <div class="molecule-art" style="left:40px;top:-10px;width:120px;height:140px" role="img" aria-label="Faint molecular structure on red"></div>
    </div>

    <div class="panel front">
      <div class="molecule-art" style="left:40px;top:70px;width:200px;height:130px" role="img" aria-label="Faint grey molecular structure backdrop"></div>
      <p class="brand-name">Copperfield Vitals</p>
      <div class="brand-rule"></div>
      <p class="tagline">Crafted With Quiet Care</p>
      <h2 class="function">Testosterone<br>Support</h2>
      <div class="rule"></div>
      <p class="herb">Tongkat Ali</p>
      <p class="category">Dietary Supplement</p>
      <p class="volume">30ml / 1 fl oz</p>
    </div>

    <div class="panel info">
      <div class="info-copy">
        <p><strong>Directions:</strong> As a dietary supplement, mix 30 grams (approx. two scoops) in eight ounces of water or any other beverage per day, or as directed by your health care practitioner.</p>
        <p><strong>Safety Warning:</strong> This is a natural product that may exhibit color, taste, and density variations from lot to lot. It contains naturally occuring nutrients; therefore amounts may vary within the pea protein and flavor profiles.</p>
      </div>
    </div>

    <div class="panel facts-panel">
      <div class="facts">
        <div class="facts-title">Supplement Facts</div>
        <div class="facts-serving">Serving Size 30 grams (approx. two scoops)<br>Servings Per Container 15</div>
        <table>
          <tr><th>Amount Per Serving</th><th></th><th class="dv">% Daily Value</th></tr>
          <tr><td>Calories</td><td>120</td><td></td></tr>
          <tr><td class="indent">Calories from Fat</td><td>15</td><td></td></tr>
          <tr><td>Total Fat</td><td>2 g</td><td class="dv">2%*</td></tr>
          <tr><td>Total Carbohydrate</td><td>2 g</td><td class="dv">&lt;1%*</td></tr>
          <tr><td>Protein (from organic pea)</td><td>20 g</td><td class="dv">40%*</td></tr>
          <tr><td>Calcium (from natural sources)</td><td>80 mg</td><td class="dv">8%</td></tr>
          <tr><td>Iron (from natural sources)</td><td>5 mg</td><td class="dv">30%</td></tr>
          <tr><td>Sodium</td><td>370 mg</td><td class="dv">15%</td></tr>
        </table>
        <div class="facts-note">*Percent Daily Values are based on a 2,000 calorie diet.</div>
      </div>
      <div class="panel-notes">
        <p>Other Ingredients: Certified organic natural flavor, certified organic stevia leaf extract.</p>
        <p class="storage">Store at room temperature.<br>Keep out of reach of children.</p>
      </div>
      <p class="maker">Manufactured for:<br>Copperfield Vitals LLC<br>Sheridan, Wyoming<br>(307) 641 3528</p>
      <p class="origin">Product of Thailand</p>
    </div>

    <div class="panel flap-bottom"></div>
  </section>

</body>
</html>
```